The Official Brackenfold App

I am looking for a poster to advertise my travel app. This poster will be displayed in shop windows, at train and bus stations. It needs to be eye catching with high quality images. This travel app will be advertised around Ireland so I am looking for a nature oriented design. I am also a local here in Killarney providing a hidden insight to travellers and take pride in our famous lakes, mountains and National Park I would love to see this concept in the poster design.
Updates

Please use https://tourlinkapp.vornetsites.com to access the website of the app! Thank you for all your work! Looking forward to your creative designs! Added Wednesday, October 11, 2017

Target Market(s)

Connected travellers and locals of Killarney

Industry/Entity Type

Travel

Logo Text

Tobar Glen Lodge B&B

Font styles to use
Sans Serif

Colors
9bcb3b
ffffff
cadf82

Requirements
Must have
• Big visual images that will capture passers by.
Nice to have
• Green and white colour scheme, attractive images and 'available on Fennet Market and Plume Shop' logos at the bottom.

```html
<!DOCTYPE html>
<html lang="en">
<head>
<meta charset="utf-8">
<title>The Official Brackenfold App – Poster</title>
<link href="https://fonts.googleapis.com/css2?family=Open+Sans:wght@400;600;700&family=Josefin+Sans:wght@400&display=swap" rel="stylesheet">
<style>
  :root{
    --green:#8dc63f;
    --green-soft:#cadf82;
    --green-text:#7cb82f;
    --white:#ffffff;
    --ink:#333333;
    --ink-soft:#555555;
    --panel:#ececec;
    --phone:#f4f4f4;
    --phone-edge:#d6d6d6;
    --black:#111111;
  }
  *{box-sizing:border-box;margin:0;padding:0}
  html,body{width:998px;height:1200px;overflow:hidden;background:var(--panel)}
  body{font-family:"Open Sans",sans-serif;color:var(--ink);position:relative}
  .poster{position:absolute;inset:0;background:linear-gradient(180deg,#efefef,#e4e4e4)}
  .hero{position:absolute;left:0;top:0;width:998px;height:520px;
    background:linear-gradient(180deg,#3f86d6 0%,#9cc6ea 30%,#7fa3a0 42%,#3f6b3a 62%,#5a6d3e 80%,#6f6a60 100%)}
  .hero-rule{position:absolute;left:0;top:520px;width:998px;height:4px;background:var(--green)}
  .app-title{position:absolute;left:150px;top:196px;width:440px;text-align:center;white-space:nowrap;
    font-family:"Josefin Sans",sans-serif;font-weight:400;font-variant:small-caps;font-size:30px;color:var(--white);letter-spacing:0.3px}

  .phone{position:absolute;background:var(--phone);border:2px solid var(--phone-edge);border-radius:34px;box-shadow:0 6px 18px rgba(0,0,0,.25)}
  .phone .speaker{position:absolute;left:50%;transform:translateX(-50%);width:34px;height:5px;border-radius:3px;background:#333}
  .phone .cam{position:absolute;left:50%;transform:translateX(-50%);width:8px;height:8px;border-radius:50%;background:#333}
  .phone .home{position:absolute;left:50%;transform:translateX(-50%);border:2px solid #555;border-radius:50%}
  .phone .screen{position:absolute;background:var(--white);overflow:hidden;border:1px solid #999}

  .phone--main{left:600px;top:50px;width:250px;height:560px}
  .phone--main .cam{top:22px}.phone--main .speaker{top:38px}
  .phone--main .home{bottom:18px;width:46px;height:46px}
  .phone--main .screen{left:15px;top:80px;width:216px;height:400px}
  .screen-bar{height:26px;display:flex;align-items:center;justify-content:center;white-space:nowrap;
    font-family:"Josefin Sans",sans-serif;font-variant:small-caps;font-size:13px;color:var(--green-text);border-bottom:1px solid #ddd}
  .tile{height:111px;display:flex;align-items:center;justify-content:center;
    font-family:"Josefin Sans",sans-serif;font-variant:small-caps;font-size:16px;color:var(--white);letter-spacing:.5px}
  .tile--atm{background:linear-gradient(180deg,#0b1b5e,#152a80)}
  .tile--time{background:linear-gradient(180deg,#4c3a2e,#7a6656)}
  .tile--gems{background:linear-gradient(180deg,#5a7a1e,#2f4a12)}
  .nav{height:41px;background:var(--green);display:flex;justify-content:space-around;align-items:center}
  .nav-item{display:flex;flex-direction:column;align-items:center;font-size:6px;color:var(--white);gap:2px;white-space:nowrap}
  .nav-item svg{width:12px;height:12px}

  .features{position:absolute;left:50px;top:528px;width:480px;height:550px;background:var(--white)}
  .features h2{position:absolute;left:22px;top:28px;font-size:26px;font-weight:700;color:#3a3a3a}
  .feature{position:absolute;left:20px;width:440px;height:90px}
  .feature svg{position:absolute;left:0;top:26px;width:48px;height:48px}
  .feature h3{position:absolute;left:66px;top:0;font-size:16px;font-weight:600;color:var(--green-text)}
  .feature p{position:absolute;left:66px;top:24px;width:370px;font-size:11.5px;line-height:1.45;color:var(--ink-soft)}

  .phone--detail{width:170px;height:370px;top:660px}
  .phone--detail .cam{top:16px}.phone--detail .speaker{top:30px}
  .phone--detail .home{bottom:10px;width:30px;height:30px}
  .phone--detail .screen{left:10px;top:52px;width:146px;height:272px}
  .phone--a{left:545px}.phone--b{left:702px}
  .detail-top{height:16px;border-bottom:1px solid #ddd;font-size:9px;padding-left:5px;line-height:15px;color:#444}
  .detail-photo{height:110px}
  .detail-photo--road{background:linear-gradient(180deg,#4f7a2f,#7d9a55 60%,#8f8a7a)}
  .detail-photo--valley{background:linear-gradient(180deg,#2f6fc4,#93b9dd 40%,#4f7d3a 70%,#6e6c5a)}
  .detail-title{font-size:9px;padding:8px 5px 2px;color:#222}
  .detail-pin{font-size:6.5px;color:var(--green-text);padding:2px 5px 4px;display:flex;align-items:center;gap:3px}
  .detail-text{font-size:6.5px;line-height:1.45;color:#666;padding:0 5px}

  .visit{position:absolute;left:60px;top:1078px;width:540px;height:48px;background:var(--green);
    display:flex;align-items:center;padding-left:40px;gap:10px;color:var(--white)}
  .visit-label{font-size:13px;font-weight:700;color:#3c5a14}
  .visit-url{font-size:14px;letter-spacing:3px}
  .available{position:absolute;left:630px;top:1048px;width:260px}
  .available-label{text-align:center;font-size:15px;font-weight:700;letter-spacing:6px;color:#222}
  .stores{display:flex;gap:12px;justify-content:center;margin-top:10px}
  .store{background:var(--black);color:var(--white);border-radius:4px;padding:8px 12px;font-size:13px;font-weight:600;display:flex;align-items:center;gap:6px}
  .store-dot{width:8px;height:8px;background:var(--white);border-radius:50%}
  .corner-block{position:absolute;left:910px;top:1040px;width:88px;height:50px;background:var(--green)}
</style>
</head>
<body>
<main class="poster">
  <section class="hero" role="img" aria-label="Photograph of two hikers with backpacks on a rocky summit overlooking green mountains, valley and sea under a blue sky"></section>
  <div class="hero-rule"></div>
  <h1 class="app-title">The Official Brackenfold App</h1>

  <div class="phone phone--main">
    <span class="cam"></span><span class="speaker"></span>
    <div class="screen">
      <div class="screen-bar">The Official Brackenfold App</div>
      <div class="tile tile--atm" role="img" aria-label="Dark blue photo tile for ATM machines">ATM Machines</div>
      <div class="tile tile--time" role="img" aria-label="Photo tile of an hourglass for timetables">Timetables</div>
      <div class="tile tile--gems" role="img" aria-label="Photo tile of green leaves for hidden gems">Hidden Gems</div>
      <nav class="nav">
        <span class="nav-item"><svg viewBox="0 0 12 12" fill="#fff"><rect x="0" y="1" width="12" height="2"/><rect x="0" y="5" width="12" height="2"/><rect x="0" y="9" width="12" height="2"/></svg>Categories</span>
        <span class="nav-item"><svg viewBox="0 0 12 12" fill="#fff"><path d="M6 11 1.2 6.2A2.8 2.8 0 0 1 6 2.4a2.8 2.8 0 0 1 4.8 3.8z"/></svg>#lovebrackenfold</span>
        <span class="nav-item"><svg viewBox="0 0 12 12" fill="#fff"><polygon points="6,0 7.6,4.2 12,4.4 8.5,7.2 9.7,11.6 6,9 2.3,11.6 3.5,7.2 0,4.4 4.4,4.2"/></svg>My Brackenfold</span>
        <span class="nav-item"><svg viewBox="0 0 12 12" fill="none" stroke="#fff" stroke-width="1.3"><rect x="1" y="2" width="10" height="9"/><line x1="1" y1="5" x2="11" y2="5"/></svg>What's On</span>
      </nav>
    </div>
    <span class="home"></span>
  </div>

  <section class="features">
    <h2>FEATURES :</h2>
    <article class="feature" style="top:80px">
      <svg viewBox="0 0 48 48" fill="none" stroke="#555" stroke-width="2"><circle cx="24" cy="24" r="15"/><ellipse cx="24" cy="24" rx="7" ry="15"/><line x1="9" y1="24" x2="39" y2="24"/><line x1="11" y1="16" x2="37" y2="16"/><line x1="11" y1="32" x2="37" y2="32"/><ellipse cx="24" cy="24" rx="22" ry="8" transform="rotate(-25 24 24)"/></svg>
      <h3>Getting Around</h3>
      <p>Local tips for getting from town to the lakes, trails and viewpoints by bus, bike, car or on foot.</p>
    </article>
    <article class="feature" style="top:172px">
      <svg viewBox="0 0 48 48"><circle cx="24" cy="24" r="20" fill="#555"/><path d="M24 12a7 7 0 0 1 7 7c0 5-7 13-7 13s-7-8-7-13a7 7 0 0 1 7-7z" fill="#fff"/><circle cx="24" cy="19" r="2.5" fill="#555"/></svg>
      <h3>Attractions</h3>
      <p>Lakes, mountains and National Park sights, with the hidden corners only locals tend to know.</p>
    </article>
    <article class="feature" style="top:264px">
      <svg viewBox="0 0 48 48" fill="none" stroke="#555" stroke-width="2"><path d="M14 12a14 14 0 0 1 20 0M18 16a8 8 0 0 1 12 0"/><circle cx="24" cy="20" r="1.5" fill="#555"/><path d="M12 26h22v6a9 9 0 0 1-9 9h-4a9 9 0 0 1-9-9z"/><path d="M34 28h3a3 3 0 0 1 0 6h-3"/><line x1="8" y1="43" x2="40" y2="43"/></svg>
      <h3>Food &amp; Cafes</h3>
      <p>Cosy cafes, pubs and restaurants in town, with opening hours and what each one does best.</p>
    </article>
    <article class="feature" style="top:356px">
      <svg viewBox="0 0 48 48" fill="none" stroke="#555" stroke-width="2"><rect x="8" y="10" width="32" height="30" rx="2"/><line x1="8" y1="18" x2="40" y2="18"/><line x1="15" y1="6" x2="15" y2="13"/><line x1="33" y1="6" x2="33" y2="13"/><path d="M14 24h4M22 24h4M30 24h4M14 30h4M22 30h4M30 30h4M14 35h4M22 35h4"/></svg>
      <h3>Timetables</h3>
      <p>Bus, train and boat times in one place, so you never miss a connection while exploring.</p>
    </article>
    <article class="feature" style="top:448px">
      <svg viewBox="0 0 48 48" fill="none" stroke="#555" stroke-width="2.2"><rect x="10" y="4" width="28" height="40" rx="2"/><text x="24" y="17" text-anchor="middle" font-family="Open Sans, sans-serif" font-size="10" font-weight="700" fill="#555" stroke="none">ATM</text><rect x="15" y="22" width="18" height="10"/><line x1="17" y1="38" x2="31" y2="38"/></svg>
      <h3>ATM Machines</h3>
      <p>Find the nearest cash machine on the map, wherever your day in the valley takes you.</p>
    </article>
  </section>

  <div class="phone phone--detail phone--a">
    <span class="cam"></span><span class="speaker"></span>
    <div class="screen">
      <div class="detail-top">&larr;</div>
      <div class="detail-photo detail-photo--road" role="img" aria-label="Photo of a horse-drawn jaunting car on a tree-lined road"></div>
      <div class="detail-title">Brackenfold Jaunting Cars Mellow Tours</div>
      <div class="detail-pin"><svg width="6" height="8" viewBox="0 0 6 8"><path d="M3 0a3 3 0 0 1 3 3c0 2-3 5-3 5S0 5 0 3a3 3 0 0 1 3-3z" fill="#7cb82f"/></svg>8 Fernhill Close, Brackenfold</div>
      <p class="detail-text">The business has grown steadily since the first jaunt in 1959 and now serves small and large groups with many tour options.</p>
    </div>
    <span class="home"></span>
  </div>

  <div class="phone phone--detail phone--b">
    <span class="cam"></span><span class="speaker"></span>
    <div class="screen">
      <div class="detail-top">&larr;</div>
      <div class="detail-photo detail-photo--valley" role="img" aria-label="Photo of a green mountain valley with lakes under a blue sky"></div>
      <div class="detail-title">Heathers View</div>
      <div class="detail-pin"><svg width="6" height="8" viewBox="0 0 6 8"><path d="M3 0a3 3 0 0 1 3 3c0 2-3 5-3 5S0 5 0 3a3 3 0 0 1 3-3z" fill="#7cb82f"/></svg>Derrylough Road, Brackenfold</div>
      <p class="detail-text">This view of the valley is one for the ages, a lookout on the mountain road with a scene you must see during your stay.</p>
    </div>
    <span class="home"></span>
  </div>

  <footer>
    <div class="visit">
      <span class="visit-label">VISIT US ON :</span>
      <svg width="16" height="16" viewBox="0 0 16 16" fill="none" stroke="#fff" stroke-width="1.3"><circle cx="8" cy="8" r="7"/><ellipse cx="8" cy="8" rx="3" ry="7"/><line x1="1" y1="8" x2="15" y2="8"/></svg>
      <span class="visit-url">www.theofficialbrackenfoldapp.com</span>
    </div>
    <div class="available">
      <div class="available-label">AVAILABLE ON</div>
      <div class="stores">
        <span class="store"><span class="store-dot"></span>Fennet Market</span>
        <span class="store"><span class="store-dot"></span>Plume Shop</span>
      </div>
    </div>
    <div class="corner-block"></div>
  </footer>
</main>
</body>
</html>
```